RW Frameworks Inc Business cards

We need business cards using our existing logo but slightly modified. Right now the logo says RW Framework Masonry. We want to keep the RW part of the design, but replace the Framework Masonry portion with "FRAMEWORKS". Please see the attached file.
Ideally this would be a blank template so we can add Different Names, titles, and phone numbers later.
On the one side we want only the logo and on the other side the detail. I'm attaching an example for you to see.
Please reach out with any other questions. Our address and other details will be given out once we find a design we like.

Target Market(s)

Construction Industry

```html
<!DOCTYPE html>
<html lang="en">
<head>
<meta charset="UTF-8">
<title>RW Frameworks Inc – Business Cards</title>
<link rel="stylesheet" href="https://fonts.googleapis.com/css2?family=Montserrat:wght@400;500;600;700&display=swap">
<style>
  :root {
    --backdrop: #e6e5e4;
    --card-white: #ffffff;
    --brand-blue: #2172bd;
    --brand-blue-soft: #3a82c6;
    --text-white: #ffffff;
    --shadow: rgba(40, 40, 50, 0.22);
  }
  * { box-sizing: border-box; margin: 0; padding: 0; }
  html, body {
    width: 1200px; height: 1200px; overflow: hidden;
    background: var(--backdrop);
    font-family: "Montserrat", sans-serif;
  }
  .canvas { position: relative; width: 1200px; height: 1200px; }
  .card {
    position: absolute; left: 285px; width: 630px; height: 360px;
    box-shadow: 0 12px 30px var(--shadow);
    overflow: hidden;
  }

  /* Front side: wordmark only */
  .card--front {
    top: 210px; background: var(--card-white);
    display: flex; align-items: center; justify-content: center;
  }
  .wordmark {
    display: flex; flex-direction: column; align-items: center;
    color: var(--brand-blue); font-weight: 600;
  }
  .wordmark__initials { font-size: 78px; line-height: 1; letter-spacing: 4px; }
  .wordmark__name { font-size: 17px; letter-spacing: 11px; margin-top: 14px; margin-right: -11px; }

  /* Back side: contact details */
  .card--back { top: 630px; background: var(--brand-blue); color: var(--text-white); }
  .back-wordmark {
    position: absolute; top: 30px; right: 36px;
    display: flex; flex-direction: column; align-items: flex-end;
    font-weight: 600;
  }
  .back-wordmark__initials { font-size: 40px; line-height: 1; letter-spacing: 2px; }
  .back-wordmark__name { font-size: 9px; letter-spacing: 6px; margin-top: 8px; margin-right: -6px; }

  .holder { position: absolute; left: 56px; top: 120px; }
  .holder__name { font-size: 28px; font-weight: 600; letter-spacing: 1px; line-height: 1; }
  .holder__title { font-size: 13px; font-weight: 400; letter-spacing: 1.5px; margin-top: 4px; margin-left: 26px; }

  .contact-list { position: absolute; left: 96px; top: 200px; list-style: none; }
  .contact-list li {
    display: flex; align-items: center; gap: 16px;
    font-size: 15px; font-weight: 500; letter-spacing: 1px;
    height: 30px;
  }
  .contact-list svg { width: 14px; height: 14px; fill: var(--text-white); }

  .website {
    position: absolute; left: 280px; bottom: 34px;
    font-size: 15px; font-weight: 600; letter-spacing: 1px;
  }
  .corner-accent {
    position: absolute; right: 0; top: 170px; width: 120px; height: 130px;
    background: linear-gradient(135deg, var(--brand-blue) 0%, var(--brand-blue-soft) 100%);
  }
</style>
</head>
<body>
<main class="canvas">

  <section class="card card--front" aria-label="Card front">
    <div class="wordmark">
      <span class="wordmark__initials">RW</span>
      <span class="wordmark__name">FRAMEWORKS</span>
    </div>
  </section>

  <section class="card card--back" aria-label="Card back">
    <div class="back-wordmark">
      <span class="back-wordmark__initials">RW</span>
      <span class="back-wordmark__name">FRAMEWORKS</span>
    </div>

    <div class="holder">
      <p class="holder__name">YOUR NAME</p>
      <p class="holder__title">PROJECT MANAGER</p>
    </div>

    <ul class="contact-list">
      <li>
        <svg viewBox="0 0 24 24" aria-hidden="true"><path d="M6.6 10.8a15.1 15.1 0 0 0 6.6 6.6l2.2-2.2a1 1 0 0 1 1-.25 11.4 11.4 0 0 0 3.6.57 1 1 0 0 1 1 1V20a1 1 0 0 1-1 1A17 17 0 0 1 3 4a1 1 0 0 1 1-1h3.5a1 1 0 0 1 1 1c0 1.250.2 2.450.57 3.57a1 1 0 0 1-.25 1z"/></svg>
        <span>Phone Number</span>
      </li>
      <li>
        <svg viewBox="0 0 24 24" aria-hidden="true"><path d="M2 5h20v14H2z M3.5 6.5 12 13l8.5-6.5" fill="var(--text-white)" stroke="var(--brand-blue)" stroke-width="1.8"/></svg>
        <span>companyname.com</span>
      </li>
      <li>
        <svg viewBox="0 0 24 24" aria-hidden="true"><path d="M12 2a7 7 0 0 0-7 7c0 5.2 7 13 7 13s7-7.8 7-13a7 7 0 0 0-7-7zm0 9.5A2.5 2.5 0 1 1 12 6.5a2.5 2.5 0 0 1 0 5z"/></svg>
        <span>Address</span>
      </li>
    </ul>

    <p class="website">www.companyname.com</p>

    <div class="corner-accent" role="img" aria-label="Corner accent area in brand blue, white and grey"></div>
  </section>

</main>
</body>
</html>
```